Streamhall Streamer Needs a Business Card Design

I need a business card design for my Streamhall stream. It's a channel that plays a variety of games but has a modern royal theme with purple, black and gold as the main colors. Font should be easily readable but have a bit of flair to it to make it stand out/be unique. Should be a bit edgy and funky, but maintain the royal theme. Only standard shaped business cards please.
Updates

- Name on the card should read Tavin Holloway, not Baron Veltrusk- Would like to see designs with and without Baron Veltrusk on the back with the logo Added Sunday, February 22, 2015

Target Market(s)

Game Developers and product makers

Industry/Entity Type

Games

Contact Information for Business Card

I would like to have the logo on the back. Contact info I need on the card would be my phone number, Streamhall, Chirpline, email, and ViewVault.

Requirements
Must have
• Name: Baron Veltrusk
• Phone Number: 401-555-0173
• Streamhall: streamhall.example/baronveltrusk
• Chirpline: @BaronVeltrusk
• Email: baronveltrusk@mailnest.example
• ViewVault: Baron Veltrusk
• Logo on the back
• "Baron Veltrusk" below logo
Nice to have
• Font should be easily readable but have a small bit of unique flair.

```html
<!DOCTYPE html>
<html lang="en">
<head>
<meta charset="UTF-8">
<title>Baron Veltrusk – Business Card</title>
<link rel="stylesheet" href="https://fonts.googleapis.com/css2?family=Cormorant+Garamond:ital,wght@1,700&family=Open+Sans:wght@300;600&display=swap">
<style>
  :root {
    --page: #ffffff;
    --card-black: #0b0b0c;
    --card-mid: #1d1e21;
    --gold: #c9962e;
    --gold-light: #f0c766;
    --gold-dark: #8a6216;
    --royal-purple: #6b2a9c;
    --text-light: #e4e4e6;
    --icon-grey: #8d8d94;
  }
  * { box-sizing: border-box; margin: 0; padding: 0; }
  html, body { width: 1200px; height: 800px; overflow: hidden; background: var(--page); }
  .canvas {
    position: relative; width: 1200px; height: 800px;
    display: flex; justify-content: center; align-items: center; gap: 80px;
  }
  .card {
    position: relative; width: 320px; height: 560px; border-radius: 22px; overflow: hidden;
    background: radial-gradient(ellipse at 50% 35%, var(--card-mid) 0%, var(--card-black) 75%);
    box-shadow: 0 10px 30px rgba(0,0,0,0.25);
  }
  .gold-rule { position: absolute; background: linear-gradient(90deg, var(--gold-dark), var(--gold-light), var(--gold)); }

  /* Front */
  .front .edge-rule { left: 30px; top: 0; width: 2px; height: 100%;
    background: linear-gradient(180deg, var(--gold-dark), var(--gold-light), var(--gold)); }
  .front .divider { left: 62px; top: 250px; width: 228px; height: 2px; }
  .brand-mark {
    position: absolute; left: 30px; right: 0; top: 70px;
    display: flex; flex-direction: column; align-items: center; gap: 14px;
  }
  .brand-dot { width: 92px; height: 92px; border-radius: 50%; background: var(--royal-purple); border: 4px solid var(--gold); }
  .brand-name { font-family: "Open Sans", sans-serif; font-weight: 600; font-size: 18px; color: var(--gold-light); letter-spacing: 1px; }

  .contact {
    position: absolute; left: 70px; top: 278px; width: 200px; height: 260px;
    writing-mode: vertical-rl;
    font-family: "Open Sans", sans-serif; color: var(--text-light);
  }
  .contact-name { font-weight: 600; font-size: 22px; font-variant: small-caps; letter-spacing: 2px; margin-left: 10px; }
  .contact-line { font-weight: 300; font-size: 15.5px; line-height: 26px; display: flex; align-items: center; gap: 8px; white-space: nowrap; }
  .contact-line svg { flex: none; }

  /* Back */
  .back .band-top { left: 0; top: 42px; width: 100%; height: 4px; }
  .back .band-bottom { left: 0; bottom: 42px; width: 100%; height: 4px; }
  .back-title {
    position: absolute; left: 30px; top: 70px; height: 420px;
    writing-mode: vertical-rl; text-align: center;
    font-family: "Cormorant Garamond", serif; font-style: italic; font-weight: 700;
    font-size: 46px; color: var(--gold);
  }
  .back .brand-mark { left: 110px; top: 200px; }
</style>
</head>
<body>
<main class="canvas">
  <section class="card front" aria-label="Card front">
    <div class="gold-rule edge-rule"></div>
    <div class="brand-mark">
      <span class="brand-dot"></span>
      <span class="brand-name">Baron Veltrusk</span>
    </div>
    <div class="gold-rule divider"></div>
    <div class="contact">
      <p class="contact-name">Tavin Holloway</p>
      <p class="contact-line">
        <svg width="14" height="14" viewBox="0 0 14 14"><rect x="2" y="2" width="10" height="10" rx="1" fill="none" stroke="var(--text-light)" stroke-width="1.4"/></svg>
        401-555-0173
      </p>
      <p class="contact-line">
        <svg width="14" height="14" viewBox="0 0 14 14"><rect x="1" y="3" width="12" height="8" fill="none" stroke="var(--text-light)" stroke-width="1.3"/><path d="M1 3 L7 8 L13 3" fill="none" stroke="var(--text-light)" stroke-width="1.3"/></svg>
        baronveltrusk@mailnest.example
      </p>
      <p class="contact-line">
        <svg width="16" height="16" viewBox="0 0 16 16"><circle cx="8" cy="8" r="7.5" fill="var(--icon-grey)"/></svg>
        @BaronVeltrusk
      </p>
      <p class="contact-line">
        <svg width="16" height="16" viewBox="0 0 16 16"><circle cx="8" cy="8" r="7.5" fill="var(--icon-grey)"/></svg>
        Baron Veltrusk
      </p>
      <p class="contact-line">
        <svg width="16" height="16" viewBox="0 0 16 16"><circle cx="8" cy="8" r="7.5" fill="var(--icon-grey)"/></svg>
        streamhall.example/baronveltrusk
      </p>
    </div>
  </section>

  <section class="card back" aria-label="Card back">
    <div class="gold-rule band-top"></div>
    <p class="back-title">Baron Veltrusk</p>
    <div class="brand-mark">
      <span class="brand-dot"></span>
      <span class="brand-name">Baron Veltrusk</span>
    </div>
    <div class="gold-rule band-bottom"></div>
  </section>
</main>
</body>
</html>
```